Brightwave Business Card

Professional Business Card Design required using the attached contact information.

Contact information can be rearranged as required.

The company is a new start up venture developing solar systems, the branding should be in keeping with that of one of the investors whose website is as follows https://www.quorvex.com/

```html
<!DOCTYPE html>
<html lang="en">
<head>
<meta charset="utf-8">
<title>Brightwave Business Card</title>
<link href="https://fonts.googleapis.com/css2?family=Montserrat:wght@500;600;700&display=swap" rel="stylesheet">
<style>
  :root {
    --green: #1a8a5a;
    --green-dark: #156e4a;
    --green-deep: #2a6f52;
    --navy: #2b3342;
    --ink: #1d2430;
    --white: #ffffff;
    --paper: #e9e7e3;
    --steel: #c9cacc;
  }
  * { margin: 0; padding: 0; box-sizing: border-box; }
  html, body { width: 1200px; height: 799px; overflow: hidden; }
  body {
    background: var(--paper);
    font-family: "Montserrat", Arial, sans-serif;
    position: relative;
  }
  .card {
    position: absolute;
    top: 245px;
    width: 540px;
    height: 309px;
    background: var(--white);
    overflow: hidden;
    box-shadow: 0 6px 18px rgba(0,0,0,0.12);
  }
  .card--brand { left: 40px; }
  .card--contact { left: 620px; }
  .card__texture {
    position: absolute;
    top: 0; right: 0;
    width: 340px; height: 240px;
    background: radial-gradient(ellipse at 70% 30%, #e2e2e2 0%, #efefef 45%, rgba(255,255,255,0) 75%);
  }
  .card--contact .card__texture {
    right: auto; left: 0; width: 100%; height: 220px;
    background: radial-gradient(ellipse at 35% 25%, #e0e0e0 0%, #eeeeee 45%, rgba(255,255,255,0) 80%);
  }
  .card__bands { position: absolute; inset: 0; }
  .wordmark {
    position: absolute;
    font-weight: 700;
    color: var(--ink);
    letter-spacing: 0.1em;
    text-transform: uppercase;
    display: flex;
    align-items: center;
    gap: 8px;
    white-space: nowrap;
  }
  .wordmark__dot {
    width: 10px; height: 10px; border-radius: 50%;
    background: var(--green);
  }
  .card--brand .wordmark { left: 70px; top: 102px; font-size: 22px; }
  .card--contact .wordmark { right: 34px; top: 24px; font-size: 14px; gap: 6px; }
  .card--contact .wordmark__dot { width: 7px; height: 7px; }
  .website {
    position: absolute;
    color: var(--white);
    font-size: 13px;
    font-weight: 600;
  }
  .card--brand .website { left: 30px; top: 189px; }
  .card--contact .website { right: 24px; top: 235px; }
  .contact {
    position: absolute;
    right: 34px;
    top: 50px;
    text-align: right;
  }
  .contact__name { color: var(--green-dark); font-size: 28px; font-weight: 600; line-height: 1.1; }
  .contact__company { color: var(--green); font-size: 15px; font-weight: 600; margin-top: 12px; }
  .contact__list { list-style: none; margin-top: 4px; }
  .contact__item {
    display: flex; justify-content: flex-end; align-items: center; gap: 6px;
    color: var(--ink); font-size: 11px; font-weight: 500; line-height: 18px;
  }
  .contact__icon { width: 12px; height: 12px; flex: none; }
</style>
</head>
<body>

<section class="card card--brand" aria-label="Card front">
  <div class="card__texture" role="img" aria-label="Soft grey halftone texture"></div>
  <svg class="card__bands" viewBox="0 0 540 309" aria-hidden="true">
    <polygon points="330,309 540,205 540,225 360,309" fill="var(--steel)"/>
    <polygon points="0,212 240,212 258,236 375,236 392,258 540,258 540,309 0,309" fill="var(--navy)"/>
    <polygon points="0,178 245,178 228,212 0,212" fill="var(--green)"/>
    <polygon points="380,309 540,232 540,309" fill="var(--green-deep)"/>
    <polygon points="450,309 540,264 540,309" fill="var(--green)"/>
  </svg>
  <div class="wordmark"><span>Brightwave</span><span class="wordmark__dot"></span><span>Renewables</span></div>
  <div class="website">www.quorvex.com</div>
</section>

<section class="card card--contact" aria-label="Card back">
  <div class="card__texture" role="img" aria-label="Soft grey halftone texture"></div>
  <svg class="card__bands" viewBox="0 0 540 309" aria-hidden="true">
    <polygon points="0,80 0,100 95,200 118,200" fill="var(--steel)"/>
    <polygon points="0,100 95,200 0,250" fill="var(--green-deep)"/>
    <polygon points="0,175 60,200 0,240" fill="var(--green)"/>
    <polygon points="0,250 95,200 125,200 150,245 275,245 295,270 540,270 540,309 0,309" fill="var(--navy)"/>
    <polygon points="290,216 540,216 540,252 306,252" fill="var(--green)"/>
  </svg>
  <div class="wordmark"><span>Brightwave</span><span class="wordmark__dot"></span><span>Renewables</span></div>
  <div class="contact">
    <div class="contact__name">Daniel Corwin</div>
    <div class="contact__company">Brightwave Renewables LLC</div>
    <ul class="contact__list">
      <li class="contact__item">318 Harbor Street, Boston, MA 02110
        <svg class="contact__icon" viewBox="0 0 12 12"><circle cx="6" cy="6" r="5.5" fill="none" stroke="var(--green)"/><path d="M6 2.6a2 2 0 0 0-2 2c0 1.5 2 4 2 4s2-2.5 2-4a2 2 0 0 0-2-2z" fill="var(--green)"/></svg></li>
      <li class="contact__item">+1 (555) 240-7316
        <svg class="contact__icon" viewBox="0 0 12 12"><circle cx="6" cy="6" r="5.5" fill="none" stroke="var(--green)"/><path d="M4 3.2l1 1.2-.5.8c.4.8 1 1.4 1.8 1.8l.8-.5 1.2 1-.6 1C5.6 8.2 3.8 6.4 3.5 4z" fill="var(--green)"/></svg></li>
      <li class="contact__item">daniel.corwin@brightwave-renewables.com
        <svg class="contact__icon" viewBox="0 0 12 12"><circle cx="6" cy="6" r="5.5" fill="none" stroke="var(--green)"/><rect x="3.2" y="4" width="5.6" height="4" fill="none" stroke="var(--green)" stroke-width="0.8"/><path d="M3.2 4L6 6.2 8.8 4" fill="none" stroke="var(--green)" stroke-width="0.8"/></svg></li>
    </ul>
  </div>
  <div class="website">www.quorvex.com</div>
</section>

</body>
</html>
```